Desk Allies Business Card

Contact Information for Business Card

Janne Voutilainen
Managing Director

3/47 Brindle Street Mitchell ACT 2911

Tel: +61 02 6257 3140
Mob: +61 0427 315 846

Email: janne@deskallies.com.au
Web: www.deskallies.com.au

Colors

Designer to choose colors to be used in the design.

Requirements
Must have
• Logo, Name, Title, Address, Telephone, Mobile, Email Address and Website
• "Desk Ally International Pty Ltd"

```html
<!DOCTYPE html>
<html lang="en">
<head>
<meta charset="utf-8">
<title>Desk Allies Business Card</title>
<link rel="stylesheet" href="https://fonts.googleapis.com/css2?family=Catamaran:wght@400;600&family=Lato:ital,wght@0,700;1,400&display=swap">
<style>
  :root {
    --brand-blue: #3279bf;
    --ink-dark: #3a3a3a;
    --paper: #ffffff;
    --backdrop: #e9e9e9;
    --card-edge: #3d3d3d;
  }
  * { box-sizing: border-box; margin: 0; padding: 0; }
  html, body { width: 1200px; height: 1200px; overflow: hidden; }
  body {
    background: var(--backdrop);
    position: relative;
    font-family: "Catamaran", sans-serif;
  }
  .card {
    position: absolute;
    left: 180px;
    width: 840px;
    height: 480px;
    border: 1px solid var(--card-edge);
    overflow: hidden;
  }
  .card--front { top: 110px; background: var(--paper); }
  .card--back { top: 610px; background: var(--brand-blue); }

  .brand {
    position: absolute;
    display: flex;
    align-items: center;
    gap: 16px;
    font-family: "Catamaran", sans-serif;
    font-weight: 600;
    text-transform: uppercase;
    letter-spacing: 0.5px;
    white-space: nowrap;
  }
  .brand__dot { border-radius: 50%; flex: none; }
  .card--front .brand {
    left: 50%; top: 90px; transform: translate(-50%, -50%);
    color: var(--brand-blue); font-size: 40px;
  }
  .card--front .brand__dot { width: 60px; height: 60px; background: var(--brand-blue); }
  .card--back .brand {
    left: 50%; top: 228px; transform: translate(-50%, -50%);
    color: var(--paper); font-size: 54px; gap: 22px;
  }
  .card--back .brand__dot { width: 82px; height: 82px; background: var(--paper); }

  .contact-band {
    position: absolute; left: 0; top: 168px;
    width: 100%; height: 210px;
    background: var(--brand-blue);
    color: var(--paper);
  }
  .person { position: absolute; left: 88px; top: 66px; }
  .person__name { font-size: 34px; font-weight: 400; line-height: 1.1; }
  .person__title { font-size: 23px; line-height: 1.3; }
  .contact-band__divider {
    position: absolute; left: 361px; top: 15px;
    width: 2px; height: 180px; background: var(--paper);
  }
  .contact-list {
    position: absolute; left: 396px; top: 36px;
    list-style: none;
  }
  .contact-list li {
    display: flex; align-items: center;
    height: 32px; font-size: 23px;
  }
  .contact-list svg { width: 18px; height: 18px; margin-right: 18px; flex: none; }

  .address {
    position: absolute; left: 0; top: 378px;
    width: 100%; height: 102px;
    display: flex; align-items: center; justify-content: center;
    font-family: "Lato", sans-serif; font-weight: 700;
    font-size: 26px; color: var(--brand-blue);
  }
  .legal-name {
    position: absolute; left: 0; top: 292px; width: 100%;
    text-align: center; color: var(--paper);
    font-size: 18px; letter-spacing: 3px; text-transform: uppercase;
  }
  .back-web {
    position: absolute; left: 0; top: 410px; width: 100%;
    text-align: center; color: var(--paper);
    font-family: "Lato", sans-serif; font-style: italic; font-size: 24px;
  }
</style>
</head>
<body>
  <section class="card card--front">
    <div class="brand"><span class="brand__dot"></span>Desk Allies</div>

    <div class="contact-band">
      <div class="person">
        <p class="person__name">Janne Voutilainen</p>
        <p class="person__title">Managing Director</p>
      </div>
      <div class="contact-band__divider"></div>
      <ul class="contact-list">
        <li>
          <svg viewBox="0 0 18 18" fill="none" stroke="#fff" stroke-width="1.6"><rect x="5" y="1" width="8" height="16" rx="1.5"/><line x1="8" y1="14.5" x2="10" y2="14.5"/></svg>
          +61 02 6257 3140
        </li>
        <li>
          <svg viewBox="0 0 18 18" fill="#fff"><path d="M4 1.5l3 3-1.8 2.2c.9 2 2.6 3.8 4.6 4.7L12 9.6l3 3-2 2.6C7.5 15 2.8 10.3 1.6 4.8z"/></svg>
          +61 0427 315 846
        </li>
        <li>
          <svg viewBox="0 0 18 18" fill="#fff"><path d="M1 4h16v11H1z"/><path d="M1 4l8 6 8-6M1 15l6-5.5M17 15l-6-5.5" stroke="#3279bf" stroke-width="1.4" fill="none"/></svg>
          janne@deskallies.com.au
        </li>
        <li>
          <svg viewBox="0 0 18 18" fill="none" stroke="#fff" stroke-width="1.3"><circle cx="9" cy="9" r="7.5"/><ellipse cx="9" cy="9" rx="3.2" ry="7.5"/><line x1="1.5" y1="9" x2="16.5" y2="9"/><line x1="2.6" y1="5" x2="15.4" y2="5"/><line x1="2.6" y1="13" x2="15.4" y2="13"/></svg>
          www.deskallies.com.au
        </li>
      </ul>
    </div>

    <p class="address">3/47 Brindle Street Mitchell ACT 2911</p>
  </section>

  <section class="card card--back">
    <div class="brand"><span class="brand__dot"></span>Desk Allies</div>
    <p class="legal-name">Desk Ally International Pty Ltd</p>
    <p class="back-web">www.deskallies.com.au</p>
  </section>
</body>
</html>
```